Business card design for modern LaneScope agency

Hello,

I need a business card design for my company Harbor9Studio.
We mainly offer Vornix LaneScope Tours (360° Photography) and it should be a business card with following details:

Name: Tobias Merland
Number: +49 160 55 82 907
Mail: tobias@harbor9studio.example
website: harbor9studio.example

Main colour that we use is the red of the logo.
It´s also important to integrate the "Vornix Gold logo" as the person on this business card is a Vornix Gold photographer.

And if possible we would also like to integrate something like send us a sms or pingwell and we call you back. As the number is german but we sell now in Vienna, Austria.

We offer a good price but very high photography quality, as we are mostly students - that´s our concept.

Maybe an idea is to integrate something 360° on the back-side of the card, for example the photo attached (just an idea) or some great design.
See flyer (attached) and harbor9studio.example for inspiration, maybe use of the photo of me (attached) in a circle or something

I´m very excited for your designs and thanks a lot in advance!! :)

Target Market(s)

Shops, hotels, shopping centers, etc. in Vienna, Austria

Industry/Entity Type

Business

Contact Information for Business Card

double-sided, use red of the logo, 360° vornix lanescope certified photographer

Font styles to use
Serif
Sans Serif

Colors
ec1f27

Requirements
Nice to have
• maybe some 360° design on back-side
• maybe include photo of me in a circle or something or sketched in red colour

```html
<!DOCTYPE html>
<html lang="en">
<head>
<meta charset="utf-8">
<title>Harbor9Studio – Business Card</title>
<link rel="stylesheet" href="https://fonts.googleapis.com/css2?family=Oswald:wght@400&family=Dosis:wght@300&family=Open+Sans:wght@400;700&display=swap">
<style>
  :root {
    --brand-red: #ec1f27;
    --brand-red-deep: #d81920;
    --paper: #ffffff;
    --band-grey: #e6e6e6;
    --panel-grey: #c9c9c9;
    --logo-grey: #9c9c9c;
    --ink: #111111;
    --callback-green: #1f9a3a;
    --stage: #f2f2f2;
  }
  html, body {
    margin: 0;
    padding: 0;
    width: 1200px;
    height: 840px;
    overflow: hidden;
    background: var(--stage);
  }
  .canvas {
    position: relative;
    width: 1200px;
    height: 840px;
  }
  .business-card {
    position: absolute;
    left: 150px;
    top: 140px;
    width: 900px;
    height: 560px;
    background: var(--paper);
    box-shadow: 0 10px 30px rgba(0,0,0,0.12);
    overflow: hidden;
  }
  .card-shapes {
    position: absolute;
    inset: 0;
  }
  .brand-lockup {
    position: absolute;
    left: 62px;
    top: 186px;
    display: flex;
    align-items: center;
    gap: 20px;
  }
  .brand-square {
    width: 150px;
    height: 130px;
    background: var(--brand-red);
  }
  .brand-name {
    font-family: "Oswald", sans-serif;
    font-weight: 400;
    font-size: 64px;
    line-height: 0.98;
    letter-spacing: 0;
    text-transform: uppercase;
    color: var(--logo-grey);
    margin: 0;
  }
  .brand-name span { display: block; }
  .contact-block {
    position: absolute;
    left: 330px;
    width: 520px;
    bottom: 40px;
    text-align: center;
  }
  .phone-number {
    font-family: "Dosis", sans-serif;
    font-weight: 300;
    font-size: 42px;
    color: var(--paper);
    letter-spacing: 0;
    margin: 0 0 12px 90px;
    text-align: left;
  }
  .callback-line {
    display: flex;
    align-items: center;
    justify-content: center;
    gap: 10px;
    font-family: "Open Sans", sans-serif;
    white-space: nowrap;
  }
  .sms-label {
    color: var(--brand-red);
    font-weight: 700;
    font-size: 15px;
    text-transform: uppercase;
  }
  .or-word {
    color: var(--ink);
    font-size: 26px;
    line-height: 1;
  }
  .callback-label {
    color: var(--callback-green);
    font-weight: 700;
    font-size: 15px;
    text-transform: uppercase;
  }
  .icon { display: block; }
</style>
</head>
<body>
<main class="canvas">
  <section class="business-card" aria-label="Harbor9Studio business card, front side">
    <svg class="card-shapes" width="900" height="560" viewBox="0 0 900 560" aria-hidden="true">
      <polygon class="diagonal-band" points="845,0 885,0 320,560 280,560" fill="var(--band-grey)"/>
      <polygon class="contact-panel" points="600,290 900,505 900,560 320,560" fill="var(--panel-grey)"/>
      <polygon class="accent-triangle" points="885,0 900,0 900,505 600,290" fill="var(--brand-red)"/>
      <polygon class="accent-shade" points="600,290 900,505 900,520 590,300" fill="var(--brand-red-deep)"/>
      <rect class="card-frame" x="13" y="13" width="874" height="534" fill="none" stroke="var(--brand-red)" stroke-width="26"/>
    </svg>

    <div class="brand-lockup">
      <div class="brand-square" aria-hidden="true"></div>
      <p class="brand-name"><span>Harbor9</span><span>Studio</span></p>
    </div>

    <div class="contact-block">
      <p class="phone-number">+49 160 55 82 907</p>
      <div class="callback-line">
        <span class="sms-label">Send us a SMS</span>
        <svg class="icon envelope-icon" width="28" height="20" viewBox="0 0 28 20" aria-hidden="true">
          <rect x="1" y="1" width="26" height="18" fill="var(--brand-red)"/>
          <path d="M1,1 L14,12 L27,1" fill="none" stroke="#ffffff" stroke-width="2"/>
        </svg>
        <span class="or-word">or</span>
        <svg class="icon messenger-dot" width="24" height="24" viewBox="0 0 24 24" aria-hidden="true">
          <circle cx="12" cy="12" r="11" fill="var(--callback-green)"/>
        </svg>
        <span class="callback-label">We call you back</span>
      </div>
    </div>
  </section>
</main>
</body>
</html>
```